UI Enhancements for California Cannabis Dispensary

We are looking to update the UI of our existing website to reflect our brand colors, and ethos on our website www.zentrobylorna.net. We would like to improve the shopping UX by redirecting users to their appropriate store. The iframes for our online storefronts are attached, and must be organized so that the user easily finds their correct store using both menu navigation and geo-based redirects. The redirects should redirect users only once, to avoid restricted access to other stores.

We want the design to be cohesive across all pages, and we want to use Geo-based redirects to direct the user to the appropriate store and provide them with a location icon in the navigation menu to search and select other stores. Our brand color is orange, please see attached color palette for exact and complimentary colors.

The design will need to be created using the WordPress Torvane theme and on page SEO should be respected (Headers, content, alt text, etc.).

Target Market(s)

Cannabis Consumers between 24-35

Industry/Entity Type

Cannabis

Font styles to use
Other font styles liked:
• Montserrat

Colors
0054AA
0677BA
7BADD7
CADEEF
E8F1F8
0094D4
00A9DD
6FCCEA
C7EBF8
E9F6FB
F0912C
F2A743
F7CA91
FBE8D2
FDF5EE
EE7325
F08F49
F5BC92
FAE3D3
FDF4ED

Requirements
Must have
• Mavrik Store iFrames (attached), Geo-based Redirects, Torvane Theme, Location Icon on navigation menu to select store, Cohesive brand colors
Nice to have
• Heavily shopping based. Use Photos from our Portfolio: https://qlnk.example/84KpwT2
Should not have
• Changes in <H1 - H4> headers or changes to existing copy

```html
<!DOCTYPE html>
<html lang="en">
<head>
<meta charset="utf-8">
<title>Zentro by Lorna – Cannabis Dispensaries</title>
<link href="https://fonts.googleapis.com/css2?family=Josefin+Sans:wght@300;400&family=Mulish:wght@400;600;700;800&display=swap" rel="stylesheet">
<style>
:root{
  --blue:#0054AA;
  --blue-deep:#0b3d73;
  --blue-mid:#0677BA;
  --orange:#EE7325;
  --orange-light:#F0912C;
  --orange-pale:#FBE8D2;
  --ink:#1c1c1c;
  --text:#444;
  --muted:#666;
  --line:#dcdcdc;
  --white:#fff;
  --gold:#F2A743;
}
*{box-sizing:border-box;margin:0;padding:0}
html,body{width:1200px;height:4216px;overflow:hidden;background:var(--white)}
body{position:relative;font-family:'Mulish',sans-serif;color:var(--ink)}
.abs{position:absolute}
.display{font-family:'Josefin Sans',sans-serif;font-weight:300;letter-spacing:1px}

/* header */
.site-header{left:0;top:0;width:1200px;height:98px;background:var(--blue-deep)}
.brand{left:144px;top:33px;color:var(--white);font-weight:800;font-size:26px;line-height:32px;display:flex;align-items:center;gap:10px}
.brand-dot{width:14px;height:14px;border-radius:50%;background:var(--orange)}
.nav-link{top:38px;color:var(--white);font-size:14px;font-weight:600}
.nav-link.active::after{content:"";position:absolute;left:-2px;right:-2px;top:25px;height:3px;background:var(--orange);border-radius:2px}
.store-pin{left:800px;top:36px}
.cart{left:826px;top:37px}
.cart-count{left:848px;top:28px;color:var(--white);font-size:11px;font-weight:700}
.search{left:868px;top:30px;width:185px;height:39px;background:var(--white);border-radius:20px;padding-left:22px;font-size:12px;color:var(--muted);line-height:39px}
.search-btn{position:absolute;right:5px;top:5px;width:29px;height:29px;border-radius:50%;background:var(--orange)}

/* hero */
.hero{left:0;top:98px;width:1200px;height:565px;background:radial-gradient(circle at 25% 40%,#8a6a4e 0,#3b2a22 35%,#141821 70%,#0b0f16 100%)}
.hero-panel{left:578px;top:224px;width:471px;height:316px;background:rgba(8,12,18,.55)}
.hero-title{left:643px;top:250px;color:var(--white);font-size:54px;line-height:58px;letter-spacing:2px}
.btn{display:flex;align-items:center;justify-content:center;border-radius:30px;font-size:13px;font-weight:700;letter-spacing:.3px;text-transform:uppercase}
.btn-brand{background:var(--orange);color:var(--white)}
.btn-outline{border:2px solid var(--orange);color:var(--blue);background:var(--white)}
.hero-btn{left:642px;top:453px;width:160px;height:55px}
.dot{left:1137px;width:9px;height:9px;border-radius:50%;background:var(--white)}
.dot.on{background:var(--orange)}

/* featured */
.section-title{left:0;width:1200px;text-align:center;font-size:42px;color:var(--ink)}
.tab{top:866px;width:154px;height:54px;border:2px solid var(--orange);border-radius:28px;display:flex;align-items:center;justify-content:center;font-size:15px;font-weight:600;color:var(--ink)}
.tab.active{background:var(--orange);color:var(--white)}
.product-card{width:291px;height:342px;border:1px solid var(--line);background:var(--white)}
.product-photo{position:absolute;left:40px;top:40px;right:40px;bottom:40px;border-radius:6px}
.product-name{font-size:17px;font-weight:700;color:var(--ink)}
.price{font-size:13px;color:var(--orange)}
.stars{display:flex;gap:4px}

/* about */
.about-photo{left:0;top:2071px;width:601px;height:663px;background:linear-gradient(160deg,#0c1622 0%,#2a2618 45%,#5a4620 60%,#0d141d 100%)}
.about-card{left:455px;top:2140px;width:601px;height:525px;background:var(--white);border-radius:24px;box-shadow:0 12px 40px rgba(0,0,0,.12)}
.about-title{left:524px;top:2214px;font-size:41px;line-height:57px;color:var(--ink)}
.about-copy{left:524px;top:2349px;width:472px;font-size:13.5px;line-height:27px;color:var(--text)}

/* instagram */
.insta-tile{width:280px;height:254px}

/* delivery */
.delivery{left:0;top:3665px;width:1200px;height:266px;background:linear-gradient(90deg,#0b3d73 0%,#0054AA 55%,#0b3d73 100%)}
.delivery-title{left:187px;top:3722px;color:var(--white);font-size:42px;letter-spacing:2px}
.delivery-copy{left:187px;top:3803px;color:var(--white);font-size:17px;line-height:28px}
.pay-card{top:3832px;width:43px;height:30px;border-radius:4px;background:var(--white)}

/* footer */
.foot{font-size:13.5px;line-height:27px;color:var(--text)}
.footer-rule{left:168px;top:4137px;width:885px;height:1px;background:var(--line)}
.copyright{left:168px;top:4168px;font-size:12.5px;color:var(--text)}
.social{top:4171px;width:14px;height:14px;border-radius:50%;background:var(--blue)}
</style>
</head>
<body>

<header class="abs site-header">
  <div class="abs brand"><span class="brand-dot"></span>Zentro by Lorna</div>
  <a class="abs nav-link active" style="left:417px">Shop Online</a>
  <a class="abs nav-link" style="left:540px">About</a>
  <a class="abs nav-link" style="left:622px">Blog</a>
  <a class="abs nav-link" style="left:692px">Corporate Info</a>
  <svg class="abs store-pin" width="16" height="22" viewBox="0 0 22 32" aria-label="Select store location"><path d="M11 1C5.5 1 1.5 5 1.5 10.3 1.5 17.5 11 30 11 30s9.5-12.5 9.5-19.7C20.5 5 16.5 1 11 1z" fill="#EE7325"/><circle cx="11" cy="10.5" r="4" fill="#fff"/></svg>
  <svg class="abs cart" width="22" height="20" viewBox="0 0 22 20" aria-label="Cart"><path d="M1 2h4l3 11h10l3-8H7" fill="none" stroke="#EE7325" stroke-width="2"/><circle cx="9" cy="17" r="1.8" fill="#EE7325"/><circle cx="17" cy="17" r="1.8" fill="#EE7325"/></svg>
  <span class="abs cart-count">0</span>
  <div class="abs search">Search
    <span class="search-btn"><svg width="29" height="29" viewBox="0 0 29 29"><circle cx="13.5" cy="13.5" r="5" fill="none" stroke="#fff" stroke-width="2"/><path d="M17 17l4 4" stroke="#fff" stroke-width="2"/></svg></span>
  </div>
</header>

<section class="abs hero" role="img" aria-label="Photo of a woman using a vape pen against soft evening bokeh lights"></section>
<div class="abs hero-panel"></div>
<h1 class="abs display hero-title">Cannabis<br>Dispensaries<br>Done Right</h1>
<a class="abs btn btn-brand hero-btn">Shop Now</a>
<span class="abs dot" style="top:345px"></span>
<span class="abs dot" style="top:366px"></span>
<span class="abs dot on" style="top:387px"></span>
<span class="abs dot" style="top:409px"></span>

<h2 class="abs display section-title" style="top:762px">FEATURED PRODUCTS</h2>
<a class="abs tab active" style="left:195px">Sacramento</a>
<a class="abs tab" style="left:359px">Redding</a>
<a class="abs tab" style="left:523px">Stockton</a>
<a class="abs tab" style="left:687px">Palm Springs</a>
<a class="abs tab" style="left:851px">Portland, OR</a>

<svg width="0" height="0" style="position:absolute"><defs><symbol id="star" viewBox="0 0 20 20"><path d="M10 1.5l2.6 5.5 6 .7-4.4 4.1 1.2 5.9L10 14.8 4.6 17.7l1.2-5.9L1.4 7.7l6-.7z" fill="#F2A743" stroke="#b86a10" stroke-width=".8"/></symbol></defs></svg>

<!-- row 1 -->
<div class="abs product-card" style="left:144px;top:976px"><div class="product-photo" role="img" aria-label="Cannabis flower bud" style="background:radial-gradient(circle,#7d7a3c 0,#b5ad78 45%,#fff 72%)"></div></div>
<div class="abs product-card" style="left:455px;top:976px"><div class="product-photo" role="img" aria-label="Vape cartridge" style="background:linear-gradient(90deg,#fff 38%,#b9651d 44%,#d89a3a 56%,#fff 62%)"></div></div>
<div class="abs product-card" style="left:766px;top:976px"><div class="product-photo" role="img" aria-label="Jar of flower with buds" style="background:radial-gradient(circle,#3b2f7a 0,#7a7446 40%,#fff 72%)"></div></div>
<div class="abs product-name" style="left:160px;top:1348px">Product Name</div><div class="abs price" style="left:160px;top:1380px">$56.75</div>
<div class="abs product-name" style="left:471px;top:1348px">Product Name</div><div class="abs price" style="left:471px;top:1380px">$56.75</div>
<div class="abs product-name" style="left:782px;top:1348px">Product Name</div><div class="abs price" style="left:782px;top:1380px">$56.75</div>
<div class="abs stars" style="left:316px;top:1350px"><svg width="17" height="17"><use href="#star"/></svg><svg width="17" height="17"><use href="#star"/></svg><svg width="17" height="17"><use href="#star"/></svg><svg width="17" height="17"><use href="#star"/></svg><svg width="17" height="17"><use href="#star"/></svg></div>
<div class="abs stars" style="left:627px;top:1350px"><svg width="17" height="17"><use href="#star"/></svg><svg width="17" height="17"><use href="#star"/></svg><svg width="17" height="17"><use href="#star"/></svg><svg width="17" height="17"><use href="#star"/></svg><svg width="17" height="17"><use href="#star"/></svg></div>
<div class="abs stars" style="left:938px;top:1350px"><svg width="17" height="17"><use href="#star"/></svg><svg width="17" height="17"><use href="#star"/></svg><svg width="17" height="17"><use href="#star"/></svg><svg width="17" height="17"><use href="#star"/></svg><svg width="17" height="17"><use href="#star"/></svg></div>

<!-- row 2 -->
<div class="abs product-card" style="left:144px;top:1429px"><div class="product-photo" role="img" aria-label="Concentrate jar with box" style="background:radial-gradient(circle at 60% 60%,#e88a2a 0,#9a9a9a 35%,#fff 72%)"></div></div>
<div class="abs product-card" style="left:455px;top:1429px"><div class="product-photo" role="img" aria-label="Pre-roll tube" style="background:linear-gradient(135deg,#fff 35%,#222 45%,#333 55%,#fff 65%)"></div></div>
<div class="abs product-card" style="left:766px;top:1429px"><div class="product-photo" role="img" aria-label="White pump bottle" style="background:radial-gradient(ellipse 30% 45% at 50% 52%,#e9e9e9 0,#f6f6f6 80%,#fff 100%)"></div></div>
<div class="abs product-name" style="left:160px;top:1801px">Product Name</div><div class="abs price" style="left:160px;top:1834px">$56.75</div>
<div class="abs product-name" style="left:471px;top:1801px">Product Name</div><div class="abs price" style="left:471px;top:1834px">$56.75</div>
<div class="abs product-name" style="left:782px;top:1801px">Product Name</div><div class="abs price" style="left:782px;top:1834px">$56.75</div>
<div class="abs stars" style="left:316px;top:1803px"><svg width="17" height="17"><use href="#star"/></svg><svg width="17" height="17"><use href="#star"/></svg><svg width="17" height="17"><use href="#star"/></svg><svg width="17" height="17"><use href="#star"/></svg><svg width="17" height="17"><use href="#star"/></svg></div>
<div class="abs stars" style="left:627px;top:1803px"><svg width="17" height="17"><use href="#star"/></svg><svg width="17" height="17"><use href="#star"/></svg><svg width="17" height="17"><use href="#star"/></svg><svg width="17" height="17"><use href="#star"/></svg><svg width="17" height="17"><use href="#star"/></svg></div>
<div class="abs stars" style="left:938px;top:1803px"><svg width="17" height="17"><use href="#star"/></svg><svg width="17" height="17"><use href="#star"/></svg><svg width="17" height="17"><use href="#star"/></svg><svg width="17" height="17"><use href="#star"/></svg><svg width="17" height="17"><use href="#star"/></svg></div>

<a class="abs btn btn-brand" style="left:520px;top:1912px;width:160px;height:57px">View More</a>

<!-- about -->
<div class="abs about-photo" role="img" aria-label="Night view of a lit golden bridge tower over a river"></div>
<div class="abs about-card"></div>
<h2 class="abs display about-title">ZENTRO BY LORNA<br>DISPENSARIES</h2>
<p class="abs about-copy">We have a simple ethos: By the culture, for the culture.&nbsp; Shop the best<br>brands at the best prices, guaranteed.We are a community-driven<br>company and welcome people from all walks of life.&nbsp; From elderly<br>medical patients to first time buyers, you will always be welcomed with<br>nothing but friendly vibes. From a small shop in Sacramento</p>
<a class="abs btn btn-brand" style="left:524px;top:2523px;width:160px;height:57px">Order Online</a>
<a class="abs btn btn-outline" style="left:692px;top:2523px;width:159px;height:57px">Read More</a>

<!-- instagram -->
<h2 class="abs display section-title" style="top:2866px">FOLLOW US ON INSTAGRAM</h2>
<div class="abs insta-tile" style="left:16px;top:2968px;background:linear-gradient(135deg,#2b2a28,#7a5a2e 60%,#1c1c1c)" role="img" aria-label="Wax container product photo"></div>
<div class="abs insta-tile" style="left:313px;top:2968px;background:linear-gradient(135deg,#3a2a1e,#a0622a 45%,#1a1410)" role="img" aria-label="Person with a lit joint at night"></div>
<div class="abs insta-tile" style="left:609px;top:2968px;background:radial-gradient(circle at 50% 50%,#f1d9d0 0,#d84a3a 50%,#6a1a14)" role="img" aria-label="Cherry gummies tin on a festive background"></div>
<div class="abs insta-tile" style="left:904px;top:2968px;background:linear-gradient(135deg,#e8e4e0,#1f2f7a 45%,#141a3a)" role="img" aria-label="Elderberry gummies package"></div>
<div class="abs insta-tile" style="left:16px;top:3240px;background:linear-gradient(160deg,#6a5632,#1c1a16 60%,#3a3020)" role="img" aria-label="Holiday countdown with wax jar"></div>
<div class="abs insta-tile" style="left:313px;top:3240px;background:linear-gradient(160deg,#e6e0d8,#8a3526 45%,#4a1c14)" role="img" aria-label="Pre-roll pack on a red knit hat"></div>
<div class="abs insta-tile" style="left:609px;top:3240px;background:linear-gradient(135deg,#1c2a20,#6a8a5a 50%,#2a3a28)" role="img" aria-label="Jar of flower on its side"></div>
<div class="abs insta-tile" style="left:904px;top:3240px;background:linear-gradient(135deg,#3a2a22,#b83a2a 45%,#1a1a1a)" role="img" aria-label="Vape products with a gift bow"></div>
<a class="abs btn btn-brand" style="left:520px;top:3539px;width:160px;height:58px">Load More</a>

<!-- delivery -->
<section class="abs delivery" role="img" aria-label="Dark blue product backdrop"></section>
<h2 class="abs display delivery-title">FREE DELIVERY</h2>
<p class="abs delivery-copy">Free Delivery on orders over $50.00<br>We accept cash, debit and all major credit cards.</p>
<a class="abs btn btn-brand" style="left:758px;top:3734px;width:159px;height:56px">Shop Now</a>
<span class="abs pay-card" style="left:758px" aria-label="Card option"></span>
<span class="abs pay-card" style="left:810px" aria-label="Card option"></span>
<span class="abs pay-card" style="left:863px" aria-label="Card option"></span>
<span class="abs pay-card" style="left:915px" aria-label="Card option"></span>
<span class="abs pay-card" style="left:968px" aria-label="Card option"></span>

<!-- footer -->
<svg class="abs" style="left:196px;top:3990px" width="22" height="32" viewBox="0 0 22 32" aria-label="Location"><path d="M11 1C5.5 1 1.5 5 1.5 10.3 1.5 17.5 11 30 11 30s9.5-12.5 9.5-19.7C20.5 5 16.5 1 11 1z" fill="#EE7325"/><circle cx="11" cy="10.5" r="4" fill="#fff"/></svg>
<p class="abs foot" style="left:234px;top:3985px">4270 Cedar Hollow Rd<br>Sacramento, CA 95819</p>
<p class="abs foot" style="left:460px;top:3985px">Stockton<br>Sacramento<br>Redding<br>Portland</p>
<p class="abs foot" style="left:624px;top:3985px">Palm Springs Dispensary<br>More Locations on the Way!</p>
<p class="abs foot" style="left:899px;top:3985px">About Zentro<br>Price Beat Policy<br>COVID-19<br>Our Blog</p>
<div class="abs footer-rule"></div>
<p class="abs copyright">© 2021 Zentro by Lorna.Al Rights Reserved &nbsp;| Privacy Policy &nbsp;| Terms</p>
<span class="abs social" style="left:874px" aria-label="Social link"></span>
<span class="abs social" style="left:903px" aria-label="Social link"></span>
<span class="abs social" style="left:931px" aria-label="Social link"></span>
<span class="abs social" style="left:959px" aria-label="Social link"></span>
<span class="abs social" style="left:986px" aria-label="Social link"></span>
<span class="abs social" style="left:1014px" aria-label="Social link"></span>

</body>
</html>
```